Business Card Design Quokka Celebration Co

on the front i would like to see the logo and my contact details. on the back i would like it to include the 3 parts to the business party planning, party hire and party supplies also with a line at the bottom (or white space) to write their appointment details.

Target Market(s)

mums and corporates

Industry/Entity Type

Business

Requirements
Must have
• logo and contact details which are: Name: Janelle, Phone: 0417263954, email: jan@quokkaevents.com.au, Website: www.quokkaevents.com.au,

```html
<!DOCTYPE html>
<html lang="en">
<head>
<meta charset="utf-8">
<title>Quokka Celebration Co — Business Card Back</title>
<link rel="stylesheet" href="https://fonts.googleapis.com/css2?family=Baumans&display=swap">
<style>
  :root {
    --card-bg: #25282a;
    --accent-orange: #f7810f;
    --note-white: #ffffff;
    --mark-faint: #2c3033;
    --mark-text: #303538;
  }
  html, body {
    margin: 0;
    padding: 0;
    overflow: hidden;
    background: var(--card-bg);
  }
  .card {
    position: relative;
    width: 1200px;
    height: 702px;
    background: var(--card-bg);
    overflow: hidden;
    font-family: "Baumans", "Trebuchet MS", sans-serif;
  }
  .brand-mark {
    position: absolute;
    left: 520px;
    top: 60px;
    width: 520px;
    height: 450px;
    display: flex;
    flex-direction: column;
    align-items: center;
    justify-content: center;
    gap: 24px;
  }
  .brand-mark__dot {
    width: 150px;
    height: 150px;
    border-radius: 50%;
    background: var(--mark-faint);
  }
  .brand-mark__name {
    font-size: 46px;
    color: var(--mark-text);
    white-space: nowrap;
  }
  .service-title {
    position: absolute;
    left: 66px;
    margin: 0;
    font-weight: 400;
    font-size: 40px;
    line-height: 1;
    color: var(--accent-orange);
  }
  .service-title--planning { top: 70px; }
  .service-title--hire { top: 262px; }
  .service-title--supplies { top: 454px; }
  .appointment-box {
    position: absolute;
    left: 246px;
    width: 901px;
    height: 122px;
    background: var(--note-white);
  }
  .appointment-box--planning { top: 119px; }
  .appointment-box--hire { top: 314px; }
  .appointment-box--supplies { top: 510px; }
</style>
</head>
<body>
  <main class="card">
    <div class="brand-mark" aria-hidden="true">
      <div class="brand-mark__dot"></div>
      <div class="brand-mark__name">Quokka Celebration Co</div>
    </div>

    <h2 class="service-title service-title--planning">Party planning</h2>
    <div class="appointment-box appointment-box--planning" aria-label="Space for appointment details"></div>

    <h2 class="service-title service-title--hire">Party hire</h2>
    <div class="appointment-box appointment-box--hire" aria-label="Space for appointment details"></div>

    <h2 class="service-title service-title--supplies">Party supplies</h2>
    <div class="appointment-box appointment-box--supplies" aria-label="Space for appointment details"></div>
  </main>
</body>
</html>
```